Brightwell Business Courses by Corvani LLC

Need source code for this app with one lesson examples copied. The app should include the copied content from Chapter 1 of "Accounting: Ledger Balance Drills" which in turn consists of 4 sub-chapters.
In addition, the app must contain copy of UI and code elements such that additional sub-chapters, additional chapters, and additional lessons can be added.

Requirements
Must have
• Source code for app must target IOS. Look and feel of the app can be identical to the reference app, Brightwell.
• No reference code available.
• The content of the lessons will be replaced with non-finance related material for internal training use.
Nice to have
• Mechanism for tracking progress for single user.
• Top level code in Swift.
• Web page implementations of Chapter 1.

```html
<!DOCTYPE html>
<html lang="en">
<head>
<meta charset="utf-8">
<title>Brightwell — Ledger Balance Drills</title>
<link href="https://fonts.googleapis.com/css2?family=Open+Sans:wght@400;600;700;800&display=swap" rel="stylesheet">
<style>
  :root {
    --page-bg: #ecebf0;
    --hero-deep: #24124a;
    --hero-mid: #3b2566;
    --hero-warm: #7a4a4a;
    --bar-dark: #2e1f4e;
    --bar-light: #44355f;
    --bar-divider: #55466f;
    --accent-gold: #e8b13a;
    --ink-purple: #3b2672;
    --ink-body: #4a4a52;
    --ink-muted: #7b7b85;
    --content-bg: #e4e4e6;
    --rule: #b9b6c6;
    --white: #ffffff;
  }
  * { box-sizing: border-box; margin: 0; padding: 0; }
  html, body { width: 846px; height: 1200px; overflow: hidden; }
  body {
    background: var(--page-bg);
    font-family: "Open Sans", sans-serif;
    position: relative;
  }
  .app-screen {
    position: absolute;
    left: 153px; top: 50px;
    width: 540px; height: 1100px;
    border-radius: 48px;
    overflow: hidden;
    background: var(--white);
    box-shadow: 0 20px 50px rgba(40, 20, 80, 0.18);
  }

  /* Hero */
  .book-hero {
    position: absolute; left: 0; top: 0;
    width: 540px; height: 324px;
    overflow: hidden;
  }
  .book-hero__art {
    position: absolute; inset: 0;
    background:
      radial-gradient(circle at 22% 62%, rgba(150, 90, 80, 0.55) 0, rgba(120, 70, 90, 0.35) 22%, rgba(36, 18, 74, 0) 48%),
      linear-gradient(180deg, var(--hero-deep) 0%, var(--hero-mid) 100%);
  }
  .book-hero__back {
    position: absolute; left: 40px; top: 34px;
  }
  .book-hero__back-rule {
    position: absolute; left: 88px; top: 30px;
    width: 1px; height: 26px; background: rgba(255,255,255,0.3);
  }
  .book-rating {
    position: absolute; left: 410px; top: 40px;
    width: 130px;
    color: var(--white);
  }
  .book-rating__value {
    font-size: 17px; font-weight: 600;
    padding-left: 14px; padding-bottom: 6px;
    border-bottom: 1px solid rgba(255,255,255,0.55);
  }
  .book-rating__stars { display: flex; gap: 5px; padding: 6px 0 0 14px; }
  .book-hero__watermark {
    position: absolute; left: 32px; top: 96px;
    font-size: 104px; font-weight: 800; letter-spacing: 8px;
    color: rgba(255,255,255,0.18);
    line-height: 1;
  }
  .book-title {
    position: absolute; left: 70px; top: 212px;
    display: flex; align-items: center; gap: 10px;
    color: var(--white);
    font-size: 23px; font-weight: 600;
  }
  .book-title__marker {
    width: 24px; height: 24px; border-radius: 50%;
    border: 2px solid var(--accent-gold);
    box-shadow: 0 0 14px rgba(232,177,58,0.8);
    position: relative;
  }
  .book-title__marker::after {
    content: ""; position: absolute; inset: 4px; border-radius: 50%;
    border: 1.5px solid var(--accent-gold);
  }
  .book-author {
    position: absolute; left: 104px; top: 248px;
    color: rgba(255,255,255,0.8); font-size: 14px;
  }

  /* Action bar */
  .action-bar {
    position: absolute; left: 0; top: 324px;
    width: 540px; height: 57px;
    display: flex;
    background: var(--bar-dark);
    color: var(--white);
    font-size: 11px; font-weight: 700; letter-spacing: 0.6px;
  }
  .action-bar__item {
    display: flex; align-items: center; justify-content: center; gap: 12px;
  }
  .action-bar__item--share { width: 97px; border-right: 1px solid var(--bar-divider); }
  .action-bar__item--read { width: 242px; }
  .action-bar__item--add { width: 201px; background: var(--bar-light); }

  /* Chapter content */
  .chapter {
    position: absolute; left: 0; top: 381px;
    width: 540px; height: 460px;
    background: var(--content-bg);
    padding: 30px 22px 0 23px;
  }
  .chapter__title {
    color: var(--ink-purple); font-size: 16px; font-weight: 700;
    margin-bottom: 20px;
  }
  .chapter__text {
    color: var(--ink-body); font-size: 12.3px; line-height: 20.5px;
    margin-bottom: 10px;
  }
  .subchapter-list { list-style: none; margin: 24px 12px 0 16px; }
  .subchapter-list__item {
    display: flex; justify-content: space-between; align-items: center;
    height: 43px;
    border-bottom: 1px solid var(--rule);
    color: var(--ink-purple); font-size: 13.5px; font-weight: 600;
    padding-right: 10px;
  }

  /* Similar books */
  .similar {
    position: absolute; left: 0; top: 841px;
    width: 540px; height: 259px;
    background: var(--white);
    border-top: 1px solid #d6d6da;
    padding: 20px 0 0 23px;
  }
  .similar__heading { color: #5a5a64; font-size: 18px; margin-bottom: 10px; }
  .similar__grid { display: flex; gap: 12px; }
  .similar-book { width: 117px; }
  .similar-book__cover { width: 117px; height: 128px; }
  .similar-book__cover--one { background: linear-gradient(160deg, #2f7c76, #1f4f4e); }
  .similar-book__cover--two { background: linear-gradient(160deg, #3e6f86, #27434f); }
  .similar-book__cover--three { background: linear-gradient(160deg, #1fa6b3, #157a86); }
  .similar-book__cover--four { background: linear-gradient(160deg, #3c6e9a, #1d3554); }
  .similar-book__title { font-size: 10.5px; font-weight: 700; color: #333; margin-top: 8px; }
  .similar-book__author { font-size: 10px; color: var(--ink-muted); }
  .home-indicator {
    position: absolute; left: 0; bottom: 0; width: 540px; height: 4px;
    background: var(--ink-purple);
  }
</style>
</head>
<body>
<main class="app-screen">
  <header class="book-hero">
    <div class="book-hero__art" role="img" aria-label="Softly blurred photograph of a wall clock in deep purple tones"></div>
    <svg class="book-hero__back" width="24" height="16" viewBox="0 0 24 16" aria-label="Back">
      <path d="M23 8H2M8 2 2 8l6 6" fill="none" stroke="rgba(255,255,255,0.5)" stroke-width="1.5"/>
    </svg>
    <div class="book-hero__back-rule"></div>
    <div class="book-rating">
      <div class="book-rating__value">4.5</div>
      <div class="book-rating__stars">
        <svg width="10" height="10" viewBox="0 0 10 10"><path d="M5 0l1.5 3.3 3.5.4-2.6 2.4.7 3.5L5 7.9 1.9 9.6l.7-3.5L0 3.7l3.5-.4z" fill="#d9d5e6"/></svg>
        <svg width="10" height="10" viewBox="0 0 10 10"><path d="M5 0l1.5 3.3 3.5.4-2.6 2.4.7 3.5L5 7.9 1.9 9.6l.7-3.5L0 3.7l3.5-.4z" fill="#d9d5e6"/></svg>
        <svg width="10" height="10" viewBox="0 0 10 10"><path d="M5 0l1.5 3.3 3.5.4-2.6 2.4.7 3.5L5 7.9 1.9 9.6l.7-3.5L0 3.7l3.5-.4z" fill="#d9d5e6"/></svg>
        <svg width="10" height="10" viewBox="0 0 10 10"><path d="M5 0l1.5 3.3 3.5.4-2.6 2.4.7 3.5L5 7.9 1.9 9.6l.7-3.5L0 3.7l3.5-.4z" fill="#d9d5e6"/></svg>
        <svg width="10" height="10" viewBox="0 0 10 10"><path d="M5 0l1.5 3.3 3.5.4-2.6 2.4.7 3.5L5 7.9 1.9 9.6l.7-3.5L0 3.7l3.5-.4z" fill="#7d7296"/></svg>
      </div>
    </div>
    <div class="book-hero__watermark" aria-hidden="true">LEDGER</div>
    <h1 class="book-title"><span class="book-title__marker"></span>Ledger Balance Drills</h1>
    <p class="book-author">by Marla Quenby</p>
  </header>

  <nav class="action-bar">
    <div class="action-bar__item action-bar__item--share">
      <svg width="22" height="22" viewBox="0 0 22 22" aria-label="Share">
        <g fill="none" stroke="#fff" stroke-width="1.3">
          <circle cx="16" cy="4" r="3"/><circle cx="5" cy="11" r="3"/><circle cx="16" cy="18" r="3"/>
          <path d="M7.6 9.6 13.4 5.4M7.6 12.4l5.8 4.2"/>
        </g>
      </svg>
    </div>
    <div class="action-bar__item action-bar__item--read">
      <svg width="26" height="18" viewBox="0 0 26 18" aria-hidden="true">
        <path d="M13 3C10 1 5 1 1 2v14c4-1 9-1 12 1 3-2 8-2 12-1V2c-4-1-9-1-12 1zM13 3v14" fill="none" stroke="#fff" stroke-width="1.3"/>
      </svg>
      READ BOOK
    </div>
    <div class="action-bar__item action-bar__item--add">
      <svg width="12" height="12" viewBox="0 0 12 12" aria-hidden="true"><path d="M6 0v12M0 6h12" stroke="#fff" stroke-width="1.5"/></svg>
      ADD TO MY LIST
    </div>
  </nav>

  <section class="chapter">
    <h2 class="chapter__title">Chapter1</h2>
    <p class="chapter__text">There are many variations of passages of Lorem Ipsum available, but the majority have suffered alteration in some form, by injected humour, or randomised words which don't look even slightly believable.</p>
    <p class="chapter__text">If you are going to use a passage of Lorem Ipsum, you need to be sure there isn't anything embarrassing hidden in the middle of text. All the Lorem Ipsum generators on the Internet tend to repeat predefined chunks as necessary, making this the first true generator on the Internet.</p>
    <ul class="subchapter-list">
      <li class="subchapter-list__item">Chapter 1.1 <svg width="6" height="10" viewBox="0 0 6 10"><path d="M1 1l4 4-4 4" fill="none" stroke="#8a86a0" stroke-width="1.2"/></svg></li>
      <li class="subchapter-list__item">Chapter 1.2 <svg width="6" height="10" viewBox="0 0 6 10"><path d="M1 1l4 4-4 4" fill="none" stroke="#8a86a0" stroke-width="1.2"/></svg></li>
      <li class="subchapter-list__item">Chapter 1.3 <svg width="6" height="10" viewBox="0 0 6 10"><path d="M1 1l4 4-4 4" fill="none" stroke="#8a86a0" stroke-width="1.2"/></svg></li>
      <li class="subchapter-list__item">Chapter 1.4 <svg width="6" height="10" viewBox="0 0 6 10"><path d="M1 1l4 4-4 4" fill="none" stroke="#8a86a0" stroke-width="1.2"/></svg></li>
    </ul>
  </section>

  <section class="similar">
    <h3 class="similar__heading">Similar Books</h3>
    <div class="similar__grid">
      <article class="similar-book">
        <div class="similar-book__cover similar-book__cover--one" role="img" aria-label="Book cover illustration in teal green"></div>
        <p class="similar-book__title">The Tally Keeper</p>
        <p class="similar-book__author">R.T. Ashvale</p>
      </article>
      <article class="similar-book">
        <div class="similar-book__cover similar-book__cover--two" role="img" aria-label="Book cover illustration in slate blue"></div>
        <p class="similar-book__title">The Tally Keeper</p>
        <p class="similar-book__author">R.T. Ashvale</p>
      </article>
      <article class="similar-book">
        <div class="similar-book__cover similar-book__cover--three" role="img" aria-label="Book cover illustration in bright turquoise"></div>
        <p class="similar-book__title">The Tally Keeper</p>
        <p class="similar-book__author">R.T. Ashvale</p>
      </article>
      <article class="similar-book">
        <div class="similar-book__cover similar-book__cover--four" role="img" aria-label="Book cover illustration in deep blue"></div>
        <p class="similar-book__title">The Tally Keeper</p>
        <p class="similar-book__author">R.T. Ashvale</p>
      </article>
    </div>
  </section>
  <div class="home-indicator"></div>
</main>
</body>
</html>
```